Design door hanger Bonaire Diving

We would like to have a design for a door hanger (See example below).
One side: Promote reef taster diving.
Other side: Promote Unlimited air/nitrox packages - lowest price guaranteed on Bonaire

We would like to inform people who rent a car with us about our air packages for diving. And non divers should be triggered to come and do a Reef Taster Dive with us. (KT Car rental and KT Dive is the same company.)

Target Market(s)

Divers and potential divers

Industry/Entity Type

Diving industry

Font styles to use
Sans Serif

Colors
0054AA
0677BA
7BADD7
CADEEF
E8F1F8
EE7325
F08F49
F5BC92
FAE3D3
FDF4ED

Requirements
Must have
• a few of the pictures included

```html
<!DOCTYPE html>
<html lang="en">
<head>
<meta charset="utf-8">
<title>KT Dive – Reef Taster Diving Door Hanger</title>
<link href="https://fonts.googleapis.com/css2?family=Montserrat:wght@700;800;900&family=Work+Sans:wght@400;500;600&display=swap" rel="stylesheet">
<style>
  :root {
    --stage: #2b2b2b;
    --paper: #f7f9fb;
    --navy: #1f2a9c;
    --ocean: #0677BA;
    --deep: #0054AA;
    --sky: #7BADD7;
    --aqua: #2ad4f0;
    --orange: #EE7325;
    --ink: #1a1a1a;
    --silhouette: #1c1c1c;
  }
  * { margin: 0; padding: 0; box-sizing: border-box; }
  html, body { width: 1200px; height: 960px; overflow: hidden; background: var(--stage); }
  .stage { position: relative; width: 1200px; height: 960px; }
  .door-hanger { position: absolute; left: 400px; top: 30px; width: 400px; height: 900px; }
  .hanger-shape { position: absolute; inset: 0; }
  .brand {
    position: absolute; left: 182px; top: 436px;
    display: flex; align-items: center; gap: 8px;
    font-family: "Montserrat", sans-serif; font-weight: 800;
    font-size: 22px; color: var(--navy); white-space: nowrap;
  }
  .brand-dot { width: 20px; height: 20px; border-radius: 50%; background: var(--orange); }
  .headline {
    position: absolute; left: 28px; top: 482px;
    font-family: "Montserrat", sans-serif; font-weight: 900;
    font-size: 42px; line-height: 0.98; letter-spacing: -0.5px;
  }
  .headline span { display: block; }
  .headline .line-dark { color: var(--ink); }
  .headline .line-orange { color: var(--orange); }
  .headline .line-navy { color: var(--navy); }
  .benefits {
    position: absolute; left: 24px; top: 632px; width: 270px;
    list-style: none;
    font-family: "Work Sans", sans-serif; font-weight: 500;
    font-size: 13px; line-height: 1.25; color: var(--ink);
  }
  .benefit { display: flex; gap: 10px; align-items: flex-start; margin-bottom: 11px; }
  .benefit.wide { width: 345px; }
  .benefit-icon { flex: 0 0 22px; width: 22px; height: 22px; }
  .web-band {
    position: absolute; left: 150px; top: 866px; width: 250px; height: 34px;
    background: var(--orange); border-radius: 17px 0 24px 0;
    display: flex; align-items: center; justify-content: center;
    font-family: "Work Sans", sans-serif; font-weight: 600; font-size: 9px;
    letter-spacing: 0.2px; color: var(--ink); text-transform: uppercase;
  }
</style>
</head>
<body>
<main class="stage">
  <article class="door-hanger">
    <svg class="hanger-shape" viewBox="0 0 400 900" width="400" height="900">
      <defs>
        <mask id="hanger-cut">
          <rect x="0" y="0" width="400" height="900" fill="black"/>
          <circle cx="200" cy="200" r="200" fill="white"/>
          <rect x="0" y="200" width="400" height="100" fill="white"/>
          <rect x="0" y="260" width="400" height="640" rx="24" fill="white"/>
          <circle cx="200" cy="190" r="105" fill="black"/>
          <rect x="200" y="200" width="220" height="88" fill="black"/>
          <circle cx="352" cy="200" r="48" fill="white"/>
        </mask>
        <linearGradient id="reef-blue" x1="0" y1="0" x2="1" y2="1">
          <stop offset="0" stop-color="#17b8f0"/>
          <stop offset="0.55" stop-color="#0677BA"/>
          <stop offset="1" stop-color="#0054AA"/>
        </linearGradient>
        <linearGradient id="turtle-photo" x1="0" y1="0" x2="0" y2="1">
          <stop offset="0" stop-color="#2a8fc9"/>
          <stop offset="1" stop-color="#cfd9dc"/>
        </linearGradient>
        <linearGradient id="seahorse-photo" x1="0" y1="0" x2="1" y2="1">
          <stop offset="0" stop-color="#b3563a"/>
          <stop offset="1" stop-color="#2fa3b8"/>
        </linearGradient>
        <linearGradient id="worm-photo" x1="0" y1="0" x2="1" y2="1">
          <stop offset="0" stop-color="#d65a9a"/>
          <stop offset="1" stop-color="#6a8a2e"/>
        </linearGradient>
      </defs>
      <g mask="url(#hanger-cut)">
        <rect x="0" y="0" width="400" height="900" fill="var(--paper)"/>
        <rect x="0" y="0" width="400" height="560" fill="url(#reef-blue)" role="img" aria-label="Photo of a school of reef fish in blue water"/>
        <path d="M0 520 C 50 400, 140 340, 250 320 C 320 305, 370 300, 400 292 L400 900 L0 900 Z" fill="var(--paper)"/>
        <path d="M80 410 C 105 430, 122 455, 130 485" fill="none" stroke="var(--deep)" stroke-width="4" stroke-linecap="round"/>
        <path d="M300 345 C 305 365, 315 385, 330 400" fill="none" stroke="var(--deep)" stroke-width="4" stroke-linecap="round"/>
        <rect x="130" y="290" width="70" height="160" rx="35" fill="var(--silhouette)" transform="rotate(22 165 370)" role="img" aria-label="Silhouette of a scuba diver descending"/>
        <path d="M330 520 L375 500 L420 522 L420 595 L372 615 L325 592 Z" fill="url(#turtle-photo)" stroke="var(--orange)" stroke-width="5" stroke-linejoin="round" role="img" aria-label="Photo of a sea turtle over sand"/>
        <path d="M305 612 L350 592 L405 612 L405 682 L352 704 L305 682 Z" fill="url(#seahorse-photo)" stroke="var(--navy)" stroke-width="5" stroke-linejoin="round" role="img" aria-label="Photo of a seahorse on coral"/>
        <path d="M340 688 L385 668 L430 690 L430 740 L385 760 L340 740 Z" fill="url(#worm-photo)" stroke="var(--aqua)" stroke-width="5" stroke-linejoin="round" role="img" aria-label="Photo of a colourful feather-duster worm"/>
      </g>
    </svg>

    <div class="brand"><span class="brand-dot"></span>KT Car rental</div>

    <h1 class="headline">
      <span class="line-dark">REEF</span>
      <span class="line-orange">TASTER</span>
      <span class="line-navy">DIVING</span>
    </h1>

    <ul class="benefits">
      <li class="benefit">
        <svg class="benefit-icon" viewBox="0 0 22 22"><circle cx="11" cy="11" r="9.5" fill="none" stroke="var(--ink)" stroke-width="1.3"/><path d="M6.5 11.5l3 3 6-6.5" fill="none" stroke="var(--ink)" stroke-width="1.5" stroke-linecap="round" stroke-linejoin="round"/></svg>
        <span>Ages 10 and up can sign up for our reef taster dive</span>
      </li>
      <li class="benefit">
        <svg class="benefit-icon" viewBox="0 0 22 22"><circle cx="11" cy="11" r="9.5" fill="none" stroke="var(--ink)" stroke-width="1.3"/><path d="M6.5 11.5l3 3 6-6.5" fill="none" stroke="var(--ink)" stroke-width="1.5" stroke-linecap="round" stroke-linejoin="round"/></svg>
        <span>The Reef Taster Diving course will take 3-4 hours</span>
      </li>
      <li class="benefit">
        <svg class="benefit-icon" viewBox="0 0 22 22"><circle cx="11" cy="11" r="9.5" fill="none" stroke="var(--ink)" stroke-width="1.3"/><path d="M6.5 11.5l3 3 6-6.5" fill="none" stroke="var(--ink)" stroke-width="1.5" stroke-linecap="round" stroke-linejoin="round"/></svg>
        <span>A group consists of a maximum of 4 people</span>
      </li>
      <li class="benefit wide">
        <svg class="benefit-icon" viewBox="0 0 22 22"><circle cx="11" cy="11" r="9.5" fill="none" stroke="var(--ink)" stroke-width="1.3"/><path d="M6.5 11.5l3 3 6-6.5" fill="none" stroke="var(--ink)" stroke-width="1.5" stroke-linecap="round" stroke-linejoin="round"/></svg>
        <span>Experience the splendor of the ocean without much distraction by other divers</span>
      </li>
      <li class="benefit wide">
        <svg class="benefit-icon" viewBox="0 0 22 22"><circle cx="11" cy="11" r="9.5" fill="none" stroke="var(--ink)" stroke-width="1.3"/><path d="M6.5 11.5l3 3 6-6.5" fill="none" stroke="var(--ink)" stroke-width="1.5" stroke-linecap="round" stroke-linejoin="round"/></svg>
        <span>Enjoy a lot of personal attention given by your instructor</span>
      </li>
    </ul>

    <div class="web-band">www.kt-dive.example/about-kt-car-rental</div>
  </article>
</main>
</body>
</html>
```